Craft Flavoured Beer Family Extension Desing

We are a Canadian craft brewery looking for the design of a new line of beer we wish to launch within an existing family of products. Our beers are high craft beers that retail for a significant price. Example, 4.49$ for 500 mL vs. 1.49$ for a 500 mL Valdermost.

The line of beer that is being designed here is for a craft flavoured beer line targeted to women. This will be light tasting beers with light fruit flavors targeted to consumers who like beer but are not ready for the strong IPA which are generally found in the craft beer offerings.

The Marisette line, which is the name of this new product, is a ''cousin'' of the existing Gaston-Ferrand Line (more info below).

Target Market(s)

60% Females 40% Males - 21 to 40 years old

Industry/Entity Type

Brewery

Requirements
Must have
• The products will be an INDIRECT family/line extension of the Gaston-Ferrand line of products (design attached). There needs to be some similarities, but it cannot be too close. There are 3 main features on the Gaston-Ferrand label (attached) : (1) the font used for the Logo; (2) the shape of the label; (3) the motif printed on the label.
• The shape of the label must be different than the current shape.
• However, the font of the logo (Gaston-Ferrand) can be the same and the motif printed on the label can be used. Using one of these elements is sufficient to link this new brand with the Gaston-Ferrand brand.
• The name of the product will be MARISETTE
Nice to have
• The bottle, the size, the ABV will be different than for the Gaston-Ferrand beers.
• There will be 3 flavours initially : Blueberry, Grapefruit and Raspberry.
• There needs to be a back label, but if you design, you can use the exact same information as there is currently.
Should not have
• We don't want any fruit pictures or designs on the labels.

```html
<!DOCTYPE html>
<html lang="en">
<head>
<meta charset="utf-8">
<title>Marisette – Flavoured Craft Beer Labels</title>
<link rel="stylesheet" href="https://fonts.googleapis.com/css2?family=Oswald:wght@700&family=Cinzel:wght@600&family=Lato:wght@400;700&display=swap">
<style>
  :root {
    --bg: #eeeeee;
    --label-white: #ffffff;
    --ink: #2a2a2a;
    --ink-soft: #6a6a6a;
    --blueberry: #1f5fb0;
    --blueberry-light: #4aa3e0;
    --raspberry: #b3202c;
    --raspberry-light: #d9525b;
    --grapefruit: #d6ad3c;
    --grapefruit-light: #f0d57a;
  }
  * { box-sizing: border-box; margin: 0; padding: 0; }
  html, body {
    width: 857px;
    height: 1200px;
    overflow: hidden;
    background: var(--bg);
  }
  .label-range {
    width: 857px;
    height: 1200px;
    display: flex;
    align-items: center;
    justify-content: center;
    gap: 22px;
  }
  .label {
    position: relative;
    width: 250px;
    height: 340px;
  }
  .label__shape {
    position: absolute;
    inset: 0;
    width: 100%;
    height: 100%;
    filter: drop-shadow(0 3px 6px rgba(0,0,0,0.18));
  }
  .label__brand {
    position: absolute;
    top: 48px;
    left: 0;
    right: 0;
    text-align: center;
    font-family: "Oswald", sans-serif;
    font-weight: 700;
    font-size: 34px;
    letter-spacing: 1px;
    color: var(--label-white);
    text-shadow: 0 2px 0 rgba(0,0,0,0.3);
  }
  .label--grapefruit .label__brand { color: var(--ink); text-shadow: none; }
  .label__flavour {
    position: absolute;
    top: 142px;
    left: 0;
    right: 0;
    text-align: center;
    font-family: "Cinzel", serif;
    font-weight: 600;
    font-size: 21px;
    letter-spacing: 2px;
    color: var(--ink);
  }
  .label__flavour::before, .label__flavour::after { content: "\00B7"; margin: 0 6px; }
  .label__origin {
    position: absolute;
    top: 120px;
    left: 0;
    right: 0;
    text-align: center;
    font-family: "Lato", sans-serif;
    font-size: 8px;
    letter-spacing: 1.5px;
    color: var(--ink-soft);
  }
  .label__specs {
    position: absolute;
    top: 184px;
    left: 40px;
    right: 40px;
    display: flex;
    justify-content: space-between;
    font-family: "Lato", sans-serif;
    font-weight: 700;
    font-size: 10px;
    letter-spacing: 0.5px;
    color: var(--ink);
  }
  .label__ornament {
    position: absolute;
    top: 212px;
    left: 95px;
    width: 60px;
    height: 14px;
    border-radius: 7px;
    background: linear-gradient(90deg, transparent, #9a9a9a, transparent);
  }
  .label__volume {
    position: absolute;
    top: 252px;
    left: 0;
    right: 0;
    text-align: center;
    font-family: "Lato", sans-serif;
    font-weight: 700;
    font-size: 11px;
    letter-spacing: 1px;
    color: var(--ink);
  }
</style>
</head>
<body>
<main class="label-range">

  <article class="label label--blueberry">
    <svg class="label__shape" viewBox="0 0 250 340" aria-hidden="true">
      <path d="M0,50 L125,8 L250,50 L250,300 Q125,345 0,300 Z" fill="var(--label-white)"/>
      <path d="M0,50 L125,8 L250,50 L250,112 L125,92 L0,112 Z" fill="var(--blueberry)"/>
      <path d="M0,112 L125,92 L250,112 L250,122 L125,102 L0,122 Z" fill="var(--blueberry-light)"/>
    </svg>
    <h2 class="label__brand">MARISETTE</h2>
    <p class="label__origin">BRASSÉE AU QUÉBEC</p>
    <p class="label__flavour">BLUEBERRY</p>
    <div class="label__specs"><span>BIÈRE / BEER</span><span>5% ALC./VOL.</span></div>
    <div class="label__ornament" role="img" aria-label="Small decorative flourish"></div>
    <p class="label__volume">500 ML</p>
  </article>

  <article class="label label--raspberry">
    <svg class="label__shape" viewBox="0 0 250 340" aria-hidden="true">
      <path d="M0,50 L125,8 L250,50 L250,300 Q125,345 0,300 Z" fill="var(--label-white)"/>
      <path d="M0,50 L125,8 L250,50 L250,112 L125,92 L0,112 Z" fill="var(--raspberry)"/>
      <path d="M0,112 L125,92 L250,112 L250,122 L125,102 L0,122 Z" fill="var(--raspberry-light)"/>
    </svg>
    <h2 class="label__brand">MARISETTE</h2>
    <p class="label__origin">BRASSÉE AU QUÉBEC</p>
    <p class="label__flavour">RASPBERRY</p>
    <div class="label__specs"><span>BIÈRE / BEER</span><span>5% ALC./VOL.</span></div>
    <div class="label__ornament" role="img" aria-label="Small decorative flourish"></div>
    <p class="label__volume">500 ML</p>
  </article>

  <article class="label label--grapefruit">
    <svg class="label__shape" viewBox="0 0 250 340" aria-hidden="true">
      <path d="M0,50 L125,8 L250,50 L250,300 Q125,345 0,300 Z" fill="var(--label-white)"/>
      <path d="M0,50 L125,8 L250,50 L250,112 L125,92 L0,112 Z" fill="var(--grapefruit)"/>
      <path d="M0,112 L125,92 L250,112 L250,122 L125,102 L0,122 Z" fill="var(--grapefruit-light)"/>
    </svg>
    <h2 class="label__brand">MARISETTE</h2>
    <p class="label__origin">BRASSÉE AU QUÉBEC</p>
    <p class="label__flavour">GRAPEFRUIT</p>
    <div class="label__specs"><span>BIÈRE / BEER</span><span>5% ALC./VOL.</span></div>
    <div class="label__ornament" role="img" aria-label="Small decorative flourish"></div>
    <p class="label__volume">500 ML</p>
  </article>

</main>
</body>
</html>
```